Self-Publisher seeking a professional Book Cover design

Paperback novel, science-fiction/mind-fiction. Title “Velder’s Hollow”. Will be published via Quillmark PPS and must meet their sizing requirements for a Book Cover (‘the spine”). (The book is 362 pages). The overall concept of design should be relatively simple, playing with themes of dark/blackness/space/unconscious/insanity-themes. Initially I had in mind a dark cover with something floating small and distant in the darkness like a sort of “space-cocoon”/hibernation-tank for an astronaut. (just something to get started thinking with). I am very open to any concepts.

From the back cover:
“In the year 3438, a discovery of a lifetime is made, and promises new light for a whole new generation of mankind which has permanently stagnated, becoming little more than slaves to their own technology which itself has already plateaued. Life goes on, yet for man, it stopped over a millennia ago. A secret project begun in the Ancient-American West in the year 1947, has catastrophic implications for the modern people’s of 3438. A discovery in space that lay apparently dormant for over a thousand years, mysteriously hidden from mankind’s ever evolving technological grasp, leads to a culture-shattering revelation that can only have one outcome. Chaos. …”

Target Market(s)

25-45 yr.

Industry/Entity Type

science-fiction, mind-bending, esotericism, psychological, space,

Font styles to use
Serif

Colors

Designer to choose colors to be used in the design.

Requirements
Must have
• darkness, with perhaps elements of bright light???
Should not have
• nothing too colorful. think, “unconscious”.

```html
<!DOCTYPE html>
<html lang="en">
<head>
<meta charset="utf-8">
<title>Velder’s Hollow — Cover</title>
<link rel="stylesheet" href="https://fonts.googleapis.com/css2?family=Cinzel:wght@400;500&display=swap">
<style>
  :root {
    --page: #ffffff;
    --cover-dark: #0a1216;
    --teal-deep: #10252c;
    --teal-mid: #2f6a70;
    --teal-glow: #8fd3cc;
    --light-core: #f4fbfa;
    --title-face: #e6f0fb;
    --title-edge: #6f9fd6;
    --author: #d9dde0;
  }
  html, body {
    margin: 0;
    padding: 0;
    width: 1200px;
    height: 1200px;
    overflow: hidden;
    background: var(--page);
  }
  .canvas {
    position: relative;
    width: 1200px;
    height: 1200px;
    background: var(--page);
  }
  .cover {
    position: absolute;
    left: 225px;
    top: 39px;
    width: 749px;
    height: 1123px;
    background: var(--cover-dark);
    overflow: hidden;
  }
  .cover-art {
    position: absolute;
    inset: 0;
    width: 100%;
    height: 100%;
    display: block;
  }
  .title {
    position: absolute;
    left: 0;
    right: 0;
    top: 62px;
    margin: 0;
    text-align: center;
    font-family: "Cinzel", "Times New Roman", serif;
    font-weight: 400;
    font-size: 128px;
    line-height: 134px;
    letter-spacing: 1px;
    color: var(--title-face);
    text-shadow: -4px 3px 0 var(--title-edge);
  }
  .title span { display: block; }
  .author {
    position: absolute;
    left: 0;
    right: 0;
    top: 1046px;
    margin: 0;
    text-align: center;
    font-family: "Cinzel", "Times New Roman", serif;
    font-weight: 400;
    font-size: 36px;
    letter-spacing: 6px;
    color: var(--author);
  }
</style>
</head>
<body>
  <main class="canvas">
    <section class="cover">
      <svg class="cover-art" viewBox="0 0 749 1123" role="img" aria-label="Cover illustration: a cloaked lone figure standing in a misty cavern before a bright glowing opening, in dark teal tones">
        <defs>
          <radialGradient id="cavern-glow" cx="0.45" cy="0.66" r="0.55">
            <stop offset="0" stop-color="var(--light-core)"/>
            <stop offset="0.14" stop-color="var(--teal-glow)"/>
            <stop offset="0.42" stop-color="var(--teal-mid)"/>
            <stop offset="0.75" stop-color="var(--teal-deep)"/>
            <stop offset="1" stop-color="var(--cover-dark)"/>
          </radialGradient>
          <linearGradient id="floor-fade" x1="0" y1="0" x2="0" y2="1">
            <stop offset="0.78" stop-color="var(--cover-dark)" stop-opacity="0"/>
            <stop offset="1" stop-color="var(--cover-dark)" stop-opacity="0.95"/>
          </linearGradient>
        </defs>
        <rect width="749" height="1123" fill="url(#cavern-glow)"/>
        <rect width="749" height="1123" fill="url(#floor-fade)"/>
      </svg>
      <h1 class="title"><span>Velder’s</span><span>Hollow</span></h1>
      <p class="author">Author Name</p>
    </section>
  </main>
</body>
</html>
```